Steady at Heart: Renew Your Team Through the 6 Habits of Balance

I'm looking for a design that is clean, like the book "Look Sideways" by Milo Brecken. The book is about the principles of organic farming so I am looking for a color scheme that fits that image.
https://www.pagelantern.example/Look-Sideways-Value-Seeing-Other-ebook/dp/Q47K520ZTR/ref=sr_1_3?crid=58XQ2PL07ZV4M&keywords=milo+brecken&qid=1638739111&s=books&sprefix=milo+%2Cstripbooks%2C371&sr=1-3

I don't want a dark color scheme. I prefer a white or cream book with a bold font.

This book is a good example of what I am looking for:

https://www.pagelantern.example/Lamp-Small-Notes-Painting-Days/dp/0912736458/ref=rtpb_2/731-5529043-4417082?pd_rd_w=mq8z3&pf_rd_p=21c9e047-385b-4f7d-a1c2-6e30b8d7f914&pf_rd_r=KP3T8QZ2207LM4NX1VA5&pd_rd_r=e63a1f20-7c4d-4a91-b5e8-09f2d1c7a6e3&pd_rd_wg=3kR2x&pd_rd_i=0912736458&psc=1

Target Market(s)

CEOs and business owners who want to increase the trust in their brands

Industry/Entity Type

Management and Leadership

Colors
00AB8E
00BBA5
67D7C9
C6EFE9
E9F9F6
59FF00
82FF00
B8FF75
E3FFCB
F4FFEA
FFF300
FFF600
FEFA6F
FFFEC7
FFFEE8
FFC000
F8CF3A
FAE287
FDF2CF
FEFAEE

Requirements
Must have
• Author's name is: Harold Vesterby
Nice to have
• I have indicated some books that I like. I would be good to have a simple image such as an apple core or the earth's core or some other image of "core" but not absolutely necessary.
Should not have
• I don't want it to have a dark cover or be too heavy

```html
<!DOCTYPE html>
<html lang="en">
<head>
<meta charset="utf-8">
<title>Steady at Heart – Cover Spread</title>
<link rel="stylesheet" href="https://fonts.googleapis.com/css2?family=Bebas+Neue&family=League+Gothic&family=Oswald:wght@200&family=Crimson+Pro:wght@400&display=swap">
<style>
  :root {
    --backdrop: #e4e4e4;
    --cream: #f1ede2;
    --ink: #2a2a2a;
    --leaf: #77c41f;
    --leaf-light: #b8e07a;
    --frame: #e6dcc2;
  }
  * { margin: 0; padding: 0; box-sizing: border-box; }
  html, body { width: 1200px; height: 960px; overflow: hidden; background: var(--backdrop); }
  .spread {
    position: absolute; left: 42px; top: 113px;
    width: 1116px; height: 734px;
    display: flex;
  }
  .cover { position: relative; width: 533px; height: 734px; background: var(--cream); overflow: hidden; }
  .spine { position: relative; width: 50px; height: 734px; background: var(--leaf); }
  .spine-text {
    position: absolute; left: 50%; top: 52px;
    transform-origin: 0 0; transform: translateX(8px) rotate(90deg);
    white-space: nowrap; color: #fff; font-size: 14px; letter-spacing: 0.2px;
  }
  .spine-title { font-family: "Bebas Neue", sans-serif; }
  .spine-author { font-family: "Oswald", sans-serif; font-weight: 200; margin-left: 12px; }

  /* back cover */
  .back-headline {
    position: absolute; left: 86px; top: 49px; width: 352px;
    font-family: "League Gothic", "Bebas Neue", sans-serif; font-weight: 400;
    font-size: 28.5px; line-height: 28.8px; color: var(--ink); letter-spacing: 0.2px;
  }
  .back-headline .line {
    display: block; white-space: nowrap;
    text-align: justify; text-align-last: justify;
  }
  .back-copy {
    position: absolute; left: 90px; width: 350px;
    font-family: "Crimson Pro", serif; font-size: 11px; line-height: 15.6px; color: var(--ink);
  }
  .back-intro { top: 176px; width: 340px; }
  .plan-heading {
    position: absolute; left: 90px; top: 243px;
    font-family: "Bebas Neue", sans-serif; font-weight: 400; font-size: 11px; color: var(--leaf);
  }
  .plan-list {
    position: absolute; left: 90px; top: 262px; width: 350px; list-style: none;
    font-family: "Crimson Pro", serif; font-size: 10.8px; line-height: 15.6px;
    color: var(--ink); letter-spacing: -0.15px;
  }
  .plan-list li { position: relative; padding-left: 22px; margin-bottom: 3.8px; }
  .plan-list svg { position: absolute; left: 2px; top: 5px; }
  .back-closing { top: 365px; }
  .back-final { top: 419px; }
  .dotted-rule {
    position: absolute; left: 49px; width: 433px; height: 4px;
    background: repeating-linear-gradient(90deg, var(--leaf) 0 1px, transparent 1px 2px);
  }
  .rule-top { top: 442px; }
  .rule-bottom { top: 618px; }
  .author-photo-frame {
    position: absolute; left: 49px; top: 461px; width: 121px; height: 138px;
    background: var(--frame); padding: 8px;
  }
  .author-photo {
    width: 100%; height: 100%;
    background: linear-gradient(180deg, #d9dde0 0%, #b7bcc2 55%, #2c3344 100%);
  }
  .author-bio {
    position: absolute; left: 180px; top: 462px; width: 304px;
    font-family: "Crimson Pro", serif; font-size: 12.2px; line-height: 17.6px; color: var(--ink);
  }
  .author-bio .bio-name { font-family: "Bebas Neue", sans-serif; font-size: 13px; }
  .back-url {
    position: absolute; left: 53px; top: 680px;
    font-family: "Bebas Neue", sans-serif; font-size: 16.5px; color: var(--ink);
  }

  /* front cover */
  .front-title {
    position: absolute; left: 50px; top: 42px; white-space: nowrap;
    font-family: "Bebas Neue", sans-serif; font-weight: 400; font-size: 84px; line-height: 1;
    color: var(--ink); letter-spacing: -1px;
  }
  .front-art {
    position: absolute; left: 55px; top: 133px; width: 300px; height: 200px;
    background:
      radial-gradient(ellipse 38% 45% at 78% 62%, #dcefb4 0%, #a9d85a 60%, rgba(241,237,226,0) 100%),
      radial-gradient(ellipse 40% 50% at 33% 46%, #b9e06a 0%, #7fc23a 65%, rgba(241,237,226,0) 100%);
  }
  .front-author {
    position: absolute; left: 48px; top: 380px; white-space: nowrap;
    font-family: "Oswald", sans-serif; font-weight: 200; font-size: 60px; line-height: 1;
    color: var(--ink); letter-spacing: -2px;
    transform: scaleX(0.84); transform-origin: 0 0;
  }
  .front-subtitle {
    position: absolute; left: 49px; top: 446px;
    font-family: "Bebas Neue", sans-serif; font-weight: 400; font-size: 76px; line-height: 61px; color: var(--ink);
  }
  .accent { color: var(--leaf); }
</style>
</head>
<body>
  <main class="spread">
    <section class="cover back-cover">
      <h2 class="back-headline">
        <span class="line">Do you need to increase repeat sales? Do you</span>
        <span class="line">wonder why other customers do not buy</span>
        <span class="line">your products at all? Have you invested in</span>
        <span class="line">certification, but it does not seem to help?</span>
      </h2>
      <p class="back-copy back-intro">This book helps you understand why you are experiencing results far below your sales potential. And it shows you how to become the brand your customers love and tell their friends about.</p>
      <h3 class="plan-heading">This book will give you a step by step plan to help you:</h3>
      <ul class="plan-list">
        <li><svg width="8" height="7" viewBox="0 0 8 7"><path d="M1 3.5 L3 5.5 L7 1" fill="none" stroke="var(--leaf)" stroke-width="1.5"/></svg>Attract and keep customers by connecting them with the larger community</li>
        <li><svg width="8" height="7" viewBox="0 0 8 7"><path d="M1 3.5 L3 5.5 L7 1" fill="none" stroke="var(--leaf)" stroke-width="1.5"/></svg>Craft authentic products that do what they say they will do and delight customers</li>
        <li><svg width="8" height="7" viewBox="0 0 8 7"><path d="M1 3.5 L3 5.5 L7 1" fill="none" stroke="var(--leaf)" stroke-width="1.5"/></svg>Increase profitability by connecting your brand to the community and the environment</li>
      </ul>
      <p class="back-copy back-closing">Thriving businesses are so much more than just “hello” and a goodbye. When you create a brand that resonates deeply with your customers and offer products they want and need, they will keep coming back and help you grow.</p>
      <p class="back-copy back-final">And it is easier than you think. Steady at Heart shows you how.</p>
      <div class="dotted-rule rule-top"></div>
      <div class="author-photo-frame">
        <div class="author-photo" role="img" aria-label="Portrait photograph of the author"></div>
      </div>
      <p class="author-bio"><span class="bio-name">Harold Vesterby</span> is CEO of TerraMark Aotearoa, the leader in organic certification for New Zealand. Born in Pinecrest Hollow, Larkmoor, he has over 25 years working in Japan, New Zealand and Asia helping high-value brands such as Wren’s Pantry, Fernbrook Fields, Tallgrass Acres, Ridgeline Bites, Sorano, Kiwara, Hoshida and Meadowleaf access foreign markets and achieve organic certification. He lives with his family in Kelburn Bay, New Zealand.</p>
      <div class="dotted-rule rule-bottom"></div>
      <p class="back-url">www.speakingbalance.example</p>
    </section>

    <section class="spine">
      <p class="spine-text"><span class="spine-title">Steady at Heart: Renew Your Team Through the 6 Habits of Balance</span><span class="spine-author">HAROLD VESTERBY</span></p>
    </section>

    <section class="cover front-cover">
      <h1 class="front-title">STEADY AT HEART:</h1>
      <div class="front-art" role="img" aria-label="Green apple with a slice cut out and a loose wedge beside it"></div>
      <p class="front-author">HAROLD VESTERBY</p>
      <p class="front-subtitle">RENEW YOUR<br>TEAM THROUGH<br>THE <span class="accent">6 HABITS</span><br>OF BALANCE</p>
    </section>
  </main>
</body>
</html>
```